Construction Company Business Card

Business Card Design using new Logo

Contact Information for Business Card

include all company info and website

Requirements
Must have
• Wesley Corman - President
ph. 254-617-0382
Cedar Knoll, TX
wesley@ironmarkframing.com
www.ironmarkframing.com

```html
<!DOCTYPE html>
<html lang="en">
<head>
<meta charset="utf-8">
<title>Ironmark Framing – Business Card</title>
<link rel="stylesheet" href="https://fonts.googleapis.com/css2?family=Arimo:wght@400;700&family=Montserrat:wght@500&display=swap">
<style>
  :root {
    --bg: #dcdcdc;
    --card-white: #ffffff;
    --brand-red: #cc2630;
    --brand-red-light: #d8404a;
    --text-grey: #a7a9ad;
    --logo-grey: #b3b5b9;
    --rule-grey: #cfd0d2;
  }
  * { margin: 0; padding: 0; box-sizing: border-box; }
  html, body { width: 1200px; height: 876px; overflow: hidden; }
  body {
    background: var(--bg);
    position: relative;
    font-family: "Arimo", Arial, sans-serif;
  }
  .card {
    position: absolute;
    left: 320px;
    width: 560px;
    height: 320px;
    border-radius: 22px;
    box-shadow: 0 6px 18px rgba(0,0,0,0.15);
    overflow: hidden;
  }
  .card--front { top: 88px; background: var(--card-white); }
  .card--back {
    top: 468px;
    background: linear-gradient(120deg, var(--brand-red) 0%, var(--brand-red-light) 45%, var(--brand-red) 100%);
    display: flex; align-items: center; justify-content: center;
  }

  /* logo lockup */
  .logo { display: flex; flex-direction: column; align-items: center; }
  .logo__row { display: flex; align-items: center; gap: 10px; }
  .logo__mark { width: 12px; height: 12px; }
  .logo__name {
    font-family: "Montserrat", Arial, sans-serif;
    font-weight: 500;
    letter-spacing: 2px;
    text-transform: uppercase;
    white-space: nowrap;
  }
  .logo__rule { height: 1.5px; margin-top: 8px; }

  .card--front .logo { position: absolute; left: 30px; top: 136px; width: 220px; }
  .card--front .logo__name { font-size: 17px; color: var(--logo-grey); }
  .card--front .logo__mark { background: var(--brand-red); }
  .card--front .logo__rule { width: 220px; background: var(--brand-red); }

  .card--back .logo__name { font-size: 26px; color: #ffffff; }
  .card--back .logo__mark { width: 16px; height: 16px; background: #ffffff; }
  .card--back .logo__rule { width: 320px; background: #ffffff; margin-top: 12px; }

  .divider {
    position: absolute; left: 272px; top: 48px;
    width: 1.5px; height: 224px; background: var(--rule-grey);
  }

  .contact { position: absolute; left: 296px; top: 66px; }
  .contact__name { color: var(--brand-red); font-weight: 700; font-size: 28px; letter-spacing: 0.3px; }
  .contact__role, .contact__place { color: var(--text-grey); font-size: 17px; margin-top: 6px; }
  .contact__list { list-style: none; margin-top: 26px; }
  .contact__item {
    display: flex; align-items: center; gap: 10px;
    color: var(--text-grey); font-size: 16px; margin-top: 7px;
  }
  .icon {
    width: 20px; height: 20px; border-radius: 5px;
    background: var(--brand-red);
    display: flex; align-items: center; justify-content: center;
    flex-shrink: 0;
  }
</style>
</head>
<body>

<section class="card card--front" aria-label="Business card front">
  <div class="logo">
    <div class="logo__row">
      <span class="logo__name">Ironmark Framing</span>
      <span class="logo__mark"></span>
    </div>
    <span class="logo__rule"></span>
  </div>

  <span class="divider"></span>

  <div class="contact">
    <p class="contact__name">Wesley Corman</p>
    <p class="contact__role">President</p>
    <p class="contact__place">Cedar Knoll, TX</p>
    <ul class="contact__list">
      <li class="contact__item">
        <span class="icon">
          <svg width="12" height="12" viewBox="0 0 24 24"><path fill="#fff" d="M6.6 10.8a15.1 15.1 0 0 0 6.6 6.6l2.2-2.2c.3-.3.7-.4 1-.2 1.1.4 2.3.6 3.6.6.6 0 1 .4 1 1V20c0 .6-.4 1-1 1A17 17 0 0 1 3 4c0-.6.4-1 1-1h3.5c.6 0 1 .4 1 1 0 1.3.2 2.5.6 3.6.1.3 0 .7-.2 1z"/></svg>
        </span>
        254-617-0382
      </li>
      <li class="contact__item">
        <span class="icon">
          <svg width="12" height="12" viewBox="0 0 24 24"><rect x="2" y="5" width="20" height="14" rx="1.5" fill="none" stroke="#fff" stroke-width="2"/><path d="M3 6l9 7 9-7" fill="none" stroke="#fff" stroke-width="2"/></svg>
        </span>
        wesley@ironmarkframing.com
      </li>
      <li class="contact__item">
        <span class="icon">
          <svg width="12" height="12" viewBox="0 0 24 24"><circle cx="12" cy="12" r="9.5" fill="none" stroke="#fff" stroke-width="2"/><ellipse cx="12" cy="12" rx="4" ry="9.5" fill="none" stroke="#fff" stroke-width="1.6"/><path d="M2.5 12h19" stroke="#fff" stroke-width="1.6"/></svg>
        </span>
        www.ironmarkframing.com
      </li>
    </ul>
  </div>
</section>

<section class="card card--back" aria-label="Business card back">
  <div class="logo">
    <div class="logo__row">
      <span class="logo__name">Ironmark Framing</span>
      <span class="logo__mark"></span>
    </div>
    <span class="logo__rule"></span>
  </div>
</section>

</body>
</html>
```